Eye Catching Email Marketing design

Our health care consulting firm is based in New York City. We sell health care consulting Services to medical practices (doctors). We need a powerful email marketing design to use as one of our primary selling tools to attract new clients. The Design should convey health care knowledge, expertise professionalism, cutting edge technology and the services we offer. <br/>The design should incorporate our logo and its colors (blue and white) but we want it to be eye catching and vibrant, so other colors be included. We are open to the designer's creativity. Any pictures used should show diversity (races)and should include women. Designers can find our logo and other graphics on our website at www harbor crest advisory.com. Please feel free to ask questions.<br/><br/>

Target Market(s)

Health care professionals, executives and Doctors.

Colors

Designer to choose colors to be used in the design.

Requirements
Nice to have
• What ever the design feels will help make this design vibrant

```html
<!DOCTYPE html>
<html lang="en">
<head>
<meta charset="utf-8">
<title>Harbor Crest Advisory – Advancing Healthcare Operations</title>
<link rel="stylesheet" href="https://fonts.googleapis.com/css2?family=Roboto:wght@400;500;700&family=Questrial&display=swap">
<style>
  :root {
    --navy: #0b4a9a;
    --sky: #2b9ad8;
    --sky-light: #3aa3df;
    --ink: #1c1c1c;
    --muted: #555;
    --white: #ffffff;
    --panel: #163f86;
  }
  * { box-sizing: border-box; margin: 0; padding: 0; }
  html, body { width: 1200px; height: 4576px; overflow: hidden; background: var(--white); }
  body { position: relative; font-family: 'Roboto', sans-serif; color: var(--ink); }
  .abs { position: absolute; }

  .hero { left: 0; top: 0; width: 1200px; height: 960px;
    background: linear-gradient(180deg, #eef2f5 0%, #cdd8e0 30%, #a8b7c4 65%, #6f7f8c 100%); }
  .brand { left: 0; top: 70px; width: 1200px; text-align: center;
    font-family: 'Roboto', sans-serif; font-weight: 500; font-size: 42px; color: var(--navy); letter-spacing: 1px; }

  .tagline-band { left: 0; top: 960px; width: 1200px; height: 200px; background: var(--sky); }
  .tagline-band .rule { position: absolute; left: 40px; right: 40px; height: 3px; background: var(--white); }
  .tagline-band h1 { position: absolute; left: 0; width: 1200px; top: 52px; text-align: center;
    color: var(--white); font-weight: 500; font-size: 60px; }

  .services-title { left: 0; top: 1262px; width: 1200px; text-align: center; font-size: 58px; font-weight: 500; color: var(--navy); }
  .services-title .lead { color: var(--sky); }

  .service { width: 532px; height: 160px; background: var(--white);
    box-shadow: 0 6px 14px rgba(0,0,0,.22); display: flex; align-items: center; }
  .service .num { width: 160px; height: 160px; display: flex; align-items: center; justify-content: center;
    color: var(--white); font-size: 62px; font-weight: 500; flex: none; }
  .service .num.navy { background: var(--navy); }
  .service .num.sky { background: var(--sky-light); }
  .service .label { padding-left: 28px; font-size: 38px; font-weight: 500; line-height: 1.2; text-transform: uppercase; color: var(--ink); }

  .help-panel { left: 0; top: 1912px; width: 652px; height: 640px; background: var(--panel); color: var(--white); }
  .help-panel h2 { position: absolute; left: 40px; top: 104px; font-size: 58px; font-weight: 700; }
  .help-panel .rule { position: absolute; left: 40px; top: 200px; width: 580px; height: 3px; background: rgba(255,255,255,.7); }
  .help-panel ul { position: absolute; left: 40px; top: 254px; list-style: none; }
  .help-panel li { font-size: 36px; line-height: 72px; text-transform: uppercase; }
  .help-panel li::before { content: "•"; margin-right: 14px; }
  .help-photo { left: 652px; top: 1912px; width: 548px; height: 640px;
    background: linear-gradient(160deg, #c9a98c 0%, #8a5a3c 45%, #e8e8ec 100%); }

  .expertise-photo { left: 0; top: 2560px; width: 640px; height: 680px;
    background: linear-gradient(90deg, #7a8a9a 0%, #b9c4cc 60%, rgba(255,255,255,1) 100%); }
  .expertise h2 { position: absolute; left: 604px; top: 2674px; width: 580px; font-size: 50px; line-height: 1.25; font-weight: 700; color: var(--navy); }
  .expertise p { position: absolute; left: 604px; top: 2836px; width: 570px; font-size: 27px; line-height: 1.75; color: var(--navy); }

  .contact-title { left: 0; top: 3310px; width: 1200px; text-align: center; font-family: 'Questrial', sans-serif; font-size: 94px; color: var(--ink); }
  .contact-rule { left: 564px; top: 3438px; width: 72px; height: 8px; background: var(--sky); }
  .contact-sub { left: 0; top: 3488px; width: 1200px; text-align: center; font-size: 52px; color: var(--navy); }

  .icon-circle { width: 160px; height: 160px; border-radius: 50%; background: var(--navy);
    display: flex; align-items: center; justify-content: center; }
  .contact-label { left: 0; width: 1200px; text-align: center; font-size: 36px; color: var(--muted); }
  .contact-value { left: 0; width: 1200px; text-align: center; font-size: 38px; font-weight: 500; color: var(--ink); }

  .subscribe { left: 448px; top: 4272px; width: 304px; height: 92px; background: var(--navy); color: var(--white);
    font-size: 36px; font-weight: 700; display: flex; align-items: center; justify-content: center; }
  .footer-rule { left: 40px; top: 4416px; width: 1120px; height: 3px; background: #333; }
  .social-dot { left: 1168px; }
  .social { left: 568px; top: 4432px; width: 64px; height: 64px; border-radius: 50%; background: var(--navy); }
  .copyright { left: 0; top: 4512px; width: 1200px; text-align: center; font-size: 30px; color: var(--ink); }
</style>
</head>
<body>
  <div class="abs hero" role="img" aria-label="Photo of a diverse medical team in discussion around a meeting table"></div>
  <div class="abs brand">Harbor Crest Advisory LLC</div>

  <section class="abs tagline-band">
    <div class="rule" style="top:28px"></div>
    <h1>Advancing Healthcare Operations</h1>
    <div class="rule" style="bottom:28px"></div>
  </section>

  <h2 class="abs services-title"><span class="lead">OUR</span> SERVICES</h2>

  <div class="abs service" style="left:48px;top:1408px"><div class="num navy">01</div><div class="label">Revenue Cycle<br>Management</div></div>
  <div class="abs service" style="left:620px;top:1408px"><div class="num sky">03</div><div class="label">Healthcare<br>Innovation</div></div>
  <div class="abs service" style="left:48px;top:1612px"><div class="num sky">02</div><div class="label">Compliance<br>Management</div></div>
  <div class="abs service" style="left:620px;top:1612px"><div class="num navy">04</div><div class="label">Practice<br>Management</div></div>

  <section class="abs help-panel">
    <h2>WE CAN HELP YOU</h2>
    <div class="rule"></div>
    <ul>
      <li>Increase Margins</li>
      <li>Integrate New Technology</li>
      <li>Transform Operations</li>
      <li>Safeguard Your Practice</li>
    </ul>
  </section>
  <div class="abs help-photo" role="img" aria-label="Photo of a smiling female doctor with a stethoscope"></div>

  <div class="abs expertise-photo" role="img" aria-label="Photo of two professionals reviewing charts at a laptop"></div>
  <section class="expertise">
    <h2>Expertise Your Medical Practice Deserves</h2>
    <p>"The expertise of our team encompasses full spectrum knowledge in revenue cycle management, practice management, regulatory compliance, and healthcare innovation."</p>
  </section>

  <h2 class="abs contact-title">Have Questions?</h2>
  <div class="abs contact-rule"></div>
  <div class="abs contact-sub">Talk to a Member of Our Team</div>

  <div class="abs icon-circle" style="left:520px;top:3592px">
    <svg width="60" height="60" viewBox="0 0 24 24" aria-hidden="true"><path fill="#fff" d="M6.6 10.8a15.1 15.1 0 0 0 6.6 6.6l2.2-2.2c.3-.3.7-.4 1-.2 1.1.4 2.3.6 3.6.6.6 0 1 .4 1 1V20c0 .6-.4 1-1 1A17 17 0 0 1 3 4c0-.6.4-1 1-1h3.5c.6 0 1 .4 1 1 0 1.3.2 2.5.6 3.6.1.3 0 .7-.2 1z"/></svg>
  </div>
  <div class="abs contact-label" style="top:3764px">Phone :</div>
  <div class="abs contact-value" style="top:3822px">(212) 555-0148</div>

  <div class="abs icon-circle" style="left:520px;top:3922px">
    <svg width="60" height="60" viewBox="0 0 24 24" aria-hidden="true"><path fill="#fff" d="M2 5h20v2l-10 6L2 7z"/><path fill="#fff" d="M2 9l10 6 10-6v10H2z"/></svg>
  </div>
  <div class="abs contact-label" style="top:4088px">Email :</div>
  <div class="abs contact-value" style="top:4150px">info@harborcrestadvisory.com</div>

  <div class="abs subscribe">Subscribe</div>
  <div class="abs footer-rule"></div>
  <div class="abs social" aria-hidden="true"></div>
  <div class="abs copyright">Copyrights @ 2020 Harbor Crest Advisory.</div>
</body>
</html>
```